WP website design for Dorrance

We need a wordpress design that will incorporate a professional color scheme with company logo in a clean layout. The design needs to consider that this will be developed on a responsive theme. Colors are will be the green of the logo and any others that will creatively highlight it.

Industry/Entity Type

It Company

Font styles to use
Sans Serif

Requirements
Must have
• Navigation: 1) Home 2) Auctions 3) Auction Services 4) Sellers 5) KT Dorrance Livestock 6) About Us 7) Contact Us
Site will have slideshow element, image attached.
Widgets will be: 1)Email Signup form 2) Featured Auctions widget 3) Social Media (FB, ClipTube, RSS) 4) News & Events blog
Footer will have smaller company logo, association logos (attached) and contact info (below)
▪ K.T. Dorrance Inc. / Auctioneers
▪ 4715 NC Hwy 91
▪ Belmora, NC 27640
▪ Office: (252) 555-0187
▪ Cell: (252) 555-0163
▪ email: ktdorrance@ktdorrance-example.com
Nice to have
• Site will have drop-down menus - please indicate the styling, for instance the dropdown menus

```html
<!DOCTYPE html>
<html lang="en">
<head>
<meta charset="utf-8">
<title>K.T. Dorrance Inc. / Auctioneers</title>
<link href="https://fonts.googleapis.com/css2?family=Roboto:wght@400;500;700&display=swap" rel="stylesheet">
<style>
:root{
  --green:#3c8c14;
  --green-dark:#2f7410;
  --text:#333;
  --muted:#777;
  --nav:#666;
  --band:#ececec;
  --panel:#f4f4f4;
  --news:#ebebeb;
  --footer:#efefee;
  --white:#fff;
  --photo-field:#7c9e3c;
  --photo-pond:#8a7f62;
  --photo-road:#8c9460;
  --photo-herd:#6e5e50;
  --photo-cow:#8a8472;
}
*{box-sizing:border-box;margin:0;padding:0}
html,body{width:1093px;height:1200px;overflow:hidden}
body{position:relative;background:var(--white);font-family:"Roboto",Arial,sans-serif;color:var(--text)}
.abs{position:absolute}
a{color:inherit;text-decoration:none}

/* header */
.brand{left:110px;top:14px;width:140px;text-align:center;color:var(--green);font-weight:500}
.brand-mark{display:block;width:46px;height:46px;border-radius:50%;background:var(--green);margin:0 auto 6px}
.brand-name{font-size:19px;line-height:22px}
.brand-sub{font-size:13px;line-height:16px}
.utility{top:10px;right:110px;display:flex;gap:28px;font-size:12px;color:var(--green)}
.utility a{display:flex;align-items:center;gap:8px}
.main-nav{top:60px;right:110px;display:flex;gap:34px;font-size:13px;color:var(--nav);letter-spacing:.3px}

/* slider */
.slider-band{left:0;top:123px;width:1093px;height:374px;background:var(--band);border-bottom:2px solid #dcdcdc}
.slider{left:109px;top:108px;width:874px;height:422px;border:1px solid #d4d4d4;border-bottom:3px solid #d0d0d0;background:var(--white);padding:1px}
.slide-photo{width:100%;height:100%;background:var(--photo-field)}
.slider-arrow{width:28px;height:28px;border-radius:50%;background:rgba(255,255,255,.8);top:328px;display:flex;align-items:center;justify-content:center}
.caption{left:139px;top:438px;width:820px;height:84px;background:rgba(48,58,30,.82);color:var(--white);padding:10px 18px}
.caption h2{font-weight:400;font-size:18px;margin-bottom:8px}
.caption p{font-size:11px;line-height:16.5px}

/* featured */
.feature-photo{left:109px;top:580px;width:198px;height:202px;border:1px solid #ccc;background:var(--photo-pond)}
.featured{left:322px;top:576px;width:400px}
.featured h2{font-size:22px;font-weight:400;color:#555}
.featured h2 strong{color:var(--green);font-weight:500}
.auction-link{display:inline-block;margin-top:4px;color:var(--green);font-size:15px;border-bottom:1px solid var(--green);line-height:17px}
.bidding{font-size:11px;color:var(--muted);margin-top:6px}
.bidding span{color:var(--green)}
.thumbs{left:324px;top:655px;display:grid;grid-template-columns:repeat(4,82px);column-gap:10px;row-gap:6px}
.thumb{height:61px}
.t-road{background:var(--photo-road)}
.t-herd{background:var(--photo-herd)}
.t-black{background:var(--photo-cow)}

/* news */
.news{left:764px;top:578px;width:220px}
.news h2{font-size:20px;font-weight:400;color:var(--green);padding-bottom:4px;border-bottom:4px solid var(--green)}
.news ul{list-style:none;background:var(--news);height:186px;padding:12px 0 0 14px}
.news li{margin-bottom:17px;padding-left:16px;position:relative}
.news li::before{content:"›";position:absolute;left:0;top:-3px;font-size:17px;color:#555}
.news .title{font-size:14px;color:var(--text)}
.news .date{display:block;font-size:10.5px;color:#999;margin-top:5px}

/* widgets */
.widgets{left:0;top:815px;width:1093px;height:223px;background:var(--panel)}
.divider{top:838px;width:1px;height:180px;background:#d6d6d6}
.widget h3{font-size:16px;font-weight:400;color:var(--green);margin-bottom:14px}
.widget p{font-size:11px;line-height:16.5px;color:var(--muted);letter-spacing:.2px}
.widget p b{color:var(--text)}
.more{display:block;margin-top:8px;font-size:11px;font-weight:700;color:var(--green)}
.field{width:175px;height:26px;border:1px solid #ccc;background:var(--white);font-size:11px;color:#888;padding:7px 10px;margin-bottom:9px}
.submit{display:inline-block;margin-top:8px;margin-left:3px;width:62px;height:23px;border-radius:3px;background:var(--green);color:var(--white);font-size:11px;text-align:center;line-height:23px;box-shadow:0 2px 0 #cfd9c6}
.connect h3{color:#555}
.social{display:flex;align-items:center;gap:10px;font-size:11px;color:#888;margin-bottom:14px}
.social .sq{width:24px;height:24px;border-radius:2px;flex:none}
.social b{font-weight:400;font-size:13.5px}

/* footer */
.footer{left:0;top:1068px;width:1093px;height:125px;background:var(--footer)}
.footer-brand{left:112px;top:1090px;width:105px;text-align:center;color:#555;font-weight:500}
.footer-brand .brand-mark{width:34px;height:34px;background:#555;margin-bottom:4px}
.footer-brand .brand-name{font-size:14px;line-height:16px}
.footer-brand .brand-sub{font-size:10.5px;line-height:13px}
.assoc{background:#d9d9d6}
.contact{top:1096px;list-style:none;font-size:11px;line-height:15.5px;color:#111}
.contact li::before{content:"• "}
.base-line{left:0;top:1193px;width:1093px;height:7px;background:var(--green)}
</style>
</head>
<body>

<header>
  <div class="brand abs"><span class="brand-mark"></span><div class="brand-name">K.T. Dorrance</div><div class="brand-sub">Inc. / Auctioneers</div></div>
  <nav class="utility abs">
    <a href="#"><svg width="22" height="20" viewBox="0 0 22 20"><rect x="1" y="1" width="20" height="18" fill="none" stroke="#555"/><rect x="10" y="8" width="2" height="8" fill="#555"/><rect x="10" y="4" width="2" height="2" fill="#555"/></svg>About Us</a>
    <a href="#"><svg width="16" height="16" viewBox="0 0 16 16"><path d="M3 1l3 3-2 2c1 2 3 4 5 5l2-2 3 3-2 3C7 15 1 9 0 4z" fill="#222"/></svg>Contact Us</a>
  </nav>
  <nav class="main-nav abs">
    <a href="#">HOME</a><a href="#">AUCTIONS</a><a href="#">AUCTION SERVICES</a><a href="#">SELLERS</a><a href="#">KT DORRANCE LIVESTOCK</a>
  </nav>
</header>

<div class="slider-band abs"></div>
<section class="slider abs">
  <div class="slide-photo" role="img" aria-label="Slideshow photo: cattle grazing in a green pasture"></div>
</section>
<span class="slider-arrow abs" style="left:136px"><svg width="10" height="12" viewBox="0 0 10 12"><path d="M7 1L2 6l5 5" fill="none" stroke="#555" stroke-width="2.5"/></svg></span>
<span class="slider-arrow abs" style="left:922px"><svg width="10" height="12" viewBox="0 0 10 12"><path d="M3 1l5 5-5 5" fill="none" stroke="#555" stroke-width="2.5"/></svg></span>
<div class="caption abs">
  <h2>Sed ut perspiciatis unde omnis iste natus error</h2>
  <p>vitae dicta sunt explicabo. Nemo enim ipsam voluptatem quia voluptas sit aspernatur aut odit aut fugit, sed quia consequuntur magni dolores eos qui ratione voluptatem sequi nesciunt. Neque porro quisquam est, qui dolorem ipsum quia dolor sit amet, consectetur, adipisci velit, sed quia non numquam</p>
</div>

<div class="feature-photo abs" role="img" aria-label="Featured auction photo: farm pond in autumn"></div>
<section class="featured abs">
  <h2>Featured Auctions <strong>widget</strong></h2>
  <a class="auction-link" href="#">Hobby Farm Auction</a>
  <p class="bidding">Bidding starts <span>march 14,2014 at 9:00am</span></p>
</section>
<div class="thumbs abs">
  <div class="thumb t-road" role="img" aria-label="Thumbnail: cattle on a farm road"></div>
  <div class="thumb t-road" role="img" aria-label="Thumbnail: cattle on a farm road"></div>
  <div class="thumb t-herd" role="img" aria-label="Thumbnail: herd of cattle in a pen"></div>
  <div class="thumb t-black" role="img" aria-label="Thumbnail: single cow standing"></div>
  <div class="thumb t-road" role="img" aria-label="Thumbnail: cattle on a farm road"></div>
  <div class="thumb t-road" role="img" aria-label="Thumbnail: cattle on a farm road"></div>
  <div class="thumb t-herd" role="img" aria-label="Thumbnail: herd of cattle in a pen"></div>
  <div class="thumb t-black" role="img" aria-label="Thumbnail: single cow standing"></div>
</div>

<aside class="news abs">
  <h2>Latest News</h2>
  <ul>
    <li><span class="title">Sed ut perspiciatis unde</span><span class="date">Sep 6,2014</span></li>
    <li><span class="title">Sed ut perspiciatis unde</span><span class="date">Sep 6,2014</span></li>
    <li><span class="title">Sed ut perspiciatis unde</span><span class="date">Sep 6,2014</span></li>
  </ul>
</aside>

<div class="widgets abs"></div>
<span class="divider abs" style="left:321px"></span>
<span class="divider abs" style="left:561px"></span>
<span class="divider abs" style="left:784px"></span>

<section class="widget abs" style="left:109px;top:840px;width:195px">
  <h3>About Us</h3>
  <p>vitae dicta sunt explicabo. Nemo enim ipsam voluptatem quia voluptas sit aspernatur aut odit aut fugit, sed quia consequuntur magni dolores eos qui ratione voluptatem sequi nesciunt. Neque porro quisquam est, qui dolorem ipsum quia dolor sit amet,</p>
</section>
<section class="widget abs" style="left:344px;top:840px;width:195px">
  <h3>Latest Blog</h3>
  <p><b>vitae dicta sunt explicabo</b>. Nemo enim ipsam voluptatem quia voluptas sit aspernatur aut odit aut fugit, sed quia consequuntur magni dolores eos qui ratione voluptatem sequi nesciunt. Neque porro quisquam est, qui dolorem ipsum quia dolor sit amet,</p>
  <a class="more" href="#">Know more</a>
</section>
<section class="widget abs" style="left:580px;top:840px;width:180px">
  <h3 style="margin-left:4px">Email Signup</h3>
  <div class="field">Name</div>
  <div class="field">Email</div>
  <div class="field">Phone</div>
  <a class="submit" href="#">Submit</a>
</section>
<section class="widget connect abs" style="left:811px;top:840px;width:190px">
  <h3>Connect with us</h3>
  <div class="social"><span class="sq" style="background:#3b5998"></span><span>Join with us on <b style="color:#3b5998">Circlebook</b></span></div>
  <div class="social"><span class="sq" style="background:#3fa9e0"></span><span>Follow us on <b style="color:#3fa9e0">Chirper</b></span></div>
  <div class="social"><span class="sq" style="background:#1d6fa5"></span><span>Share on <b style="color:#1d6fa5">WorkLink</b></span></div>
  <div class="social"><span class="sq" style="background:#c4302b"></span><span>Watch on <b style="color:#c4302b">ClipTube</b></span></div>
</section>

<footer>
  <div class="footer abs"></div>
  <div class="footer-brand abs"><span class="brand-mark"></span><div class="brand-name">K.T. Dorrance</div><div class="brand-sub">Inc. / Auctioneers</div></div>
  <span class="assoc abs" style="left:276px;top:1104px;width:96px;height:42px;border-radius:4px"></span>
  <span class="assoc abs" style="left:389px;top:1098px;width:72px;height:52px;border-radius:4px"></span>
  <span class="assoc abs" style="left:481px;top:1092px;width:70px;height:70px;border-radius:50%"></span>
  <ul class="contact abs" style="left:646px">
    <li>K.T. Dorrance Inc. / Auctioneers</li>
    <li>4715 NC Hwy 91</li>
    <li>Belmora, NC 27640</li>
  </ul>
  <ul class="contact abs" style="left:821px">
    <li>Office: (252) 555-0187</li>
    <li>Cell: (252) 555-0163</li>
    <li>email: ktdorrance@ktdorrance-example.com</li>
  </ul>
  <div class="base-line abs"></div>
</footer>

</body>
</html>
```